Fine Art business needs new website

We need a simple website with a home page, about us page, New sculptures, Sold sculptures, and a contact us page.Our sculptures are very high end one of a kind pieces. As such we need the site to be VERY elegant and professional. Lastly, because I'll be updating pictures on the website on a monthly basis it needs to be user friendly to update (Wordpress is preferred). The only branding we have so far for the business is a business card.
Updates
I wasn't completely ready when this project launched, also I am on the road right now and haven't been able to be as responsive to all you designers as I would like. I will work on giving feedback to all the top designs we've received so far. Thank you all so much for your participation and hardwork.
Target Market(s)
High end customers (affluent), art collectors, interior decorators/designers
Industry/Entity Type
Art Gallery
Coding
Coded - Design and coding required
Number of Pages Required
5+ page
Requirements
Must have
- Easily editable picture gallery for myself so that I can add new pieces(pictures of the pieces), remove sold pieces, etc. I would like the website to be built in wordpress so I can update it. I currently use sitekeeperpro through Netbirch for my other business website and would like to do the same for this one.
- Pages:
- -Intro page with featured pieces
- -Current pieces gallery (for sale) mainly a picture gallery
- -Sculptures archive (sold pieces) another picture gallery
- -About us: Pull-down of -about the artist (attached content)
- -Artistic Process (attached content)
- -Show Schedule:
- -one page dedicated to "friends of QMW" (basically a link page)
- TO BE CLEAR "www.lanternhollow.com" IS A TOTALLY DIFFERENT SITE AND I'M NOT TRYING TO COMBINE THE TWO OR JOIN THEM INTO ONE. This page needs be more elegant and seperate from the Lantern Hollow site.
- UPDATE: I'd like a link to the QMW Facebook page: https://www.facebook.com/quillmarkworks/
Nice to have
- I would like the pictures on the gallery pages able to have text connected with them (Materials, price)
- I would like the site style and fonts to be similar to our business cards we've already had designed (picture attached).
Should not have
- Too much flash or other things that will make the site slow to load.

```html
<!DOCTYPE html>
<html lang="en">
<head>
<meta charset="utf-8">
<title>QMW — Testimonials &amp; Contact</title>
<link rel="stylesheet" href="https://fonts.googleapis.com/css2?family=Montserrat:wght@500;600;700&family=Poppins:wght@300;400;500&family=EB+Garamond&display=swap">
<style>
:root{
  --ink:#2a3140;
  --title:#333333;
  --muted:#7a7a7a;
  --soft:#9a9a9a;
  --band:#f8f8f8;
  --white:#ffffff;
  --line:#e6e6e6;
  --avatar:#c9c9c9;
  --dot:#dcdcdc;
  --button:#283040;
}
*{margin:0;padding:0;box-sizing:border-box}
html,body{width:1200px;height:1200px;overflow:hidden;background:var(--white)}
body{position:relative;font-family:'Poppins',sans-serif;color:var(--ink)}
.abs{position:absolute}

.testimonials{left:0;top:40px;width:1192px;height:438px;background:var(--band)}
.testimonial-card{left:370px;top:40px;width:468px;height:258px;background:var(--white)}
.section-title{left:370px;top:78px;width:468px;text-align:center;font-family:'Montserrat',sans-serif;font-weight:700;font-size:37px;letter-spacing:12px;padding-left:12px;color:var(--title);line-height:44px}
.quote{left:390px;top:173px;width:428px;text-align:center;font-weight:300;font-size:18px;line-height:27px;color:var(--muted)}
.avatar{left:553px;top:285px;width:102px;height:102px;border-radius:50%;background:var(--avatar);box-shadow:0 2px 6px rgba(0,0,0,.15);border:2px solid var(--white)}
.author-name{left:400px;top:401px;width:408px;text-align:center;font-weight:500;font-size:19px;color:var(--ink)}
.author-role{left:400px;top:431px;width:408px;text-align:center;font-size:15.5px;color:var(--muted)}

.slider-dots{left:0;top:506px;width:1208px;display:flex;justify-content:center;align-items:center;gap:6px}
.slider-dots span{width:7px;height:7px;border-radius:50%;background:var(--dot)}
.slider-dots .active{width:20px;height:6px;border-radius:2px;background:#1e1e1e}

.eyebrow{left:0;top:646px;width:1208px;text-align:center;font-family:'Montserrat',sans-serif;font-weight:600;font-size:10px;letter-spacing:2.5px;color:#222}
.contact-title{left:0;top:666px;width:1208px;text-align:center;font-family:'Montserrat',sans-serif;font-weight:600;font-size:26px;letter-spacing:7px;color:var(--ink)}
.contact-details{left:0;top:744px;width:1208px;text-align:center;font-family:'EB Garamond',serif;font-size:17.5px;color:#555;word-spacing:1px}
.contact-details .sep{margin:0 20px}

.field{border-bottom:1px solid var(--line);height:28px;font-size:11px;color:var(--muted)}
.field-name{left:240px;top:881px;width:229px}
.field-email{left:488px;top:881px;width:229px}
.field-phone{left:736px;top:881px;width:229px}
.field-message{left:240px;top:965px;width:725px}
.submit{left:545px;top:1013px;width:117px;height:34px;background:var(--button);color:var(--white);font-family:'Montserrat',sans-serif;font-weight:600;font-size:9px;letter-spacing:1.8px;display:flex;align-items:center;justify-content:center}

.footer{left:0;top:1126px;width:1200px;height:74px;background:var(--band);border-top:1px solid #eeeeee}
.social{left:20px;top:1160px;display:flex;align-items:center;gap:16px;font-size:11px;color:#6c6c6c}
.footer-nav{left:453px;top:1164px;display:flex;gap:49px;font-family:'Montserrat',sans-serif;font-weight:600;font-size:8.5px;letter-spacing:1.8px;color:#222}
.copyright{right:24px;top:1161px;font-size:10px;color:#6c6c6c}
</style>
</head>
<body>

<section class="abs testimonials"></section>
<div class="abs testimonial-card"></div>
<h2 class="abs section-title">TESTIMONIALS</h2>
<p class="abs quote">“Let me say something. You have an amazing theme and amazing/awesome support. They helped me on weekend. ”</p>
<div class="abs avatar" role="img" aria-label="Client portrait"></div>
<p class="abs author-name">Celia Marsh</p>
<p class="abs author-role">Co-Founder / Harbor Vale Co</p>

<div class="abs slider-dots"><span></span><span class="active"></span><span></span></div>

<p class="abs eyebrow">CONTACT</p>
<h2 class="abs contact-title">KEEP IN TOUCH WITH US</h2>
<p class="abs contact-details">(555) 214-3908<span class="sep">|</span>mara@lanternhollow.com<span class="sep">|</span>www.quillmarkworks.com</p>

<div class="abs field field-name">Your Name</div>
<div class="abs field field-email">Your Email</div>
<div class="abs field field-phone">Your Phone</div>
<div class="abs field field-message">Your Message</div>
<div class="abs submit">SUBMIT NOW</div>

<footer class="abs footer"></footer>
<div class="abs social">
  <span>Feed</span><span>Notes</span><span>Boards</span><span>Network</span>
  <svg width="18" height="14" viewBox="0 0 18 14" aria-label="Email">
    <rect x="0.5" y="0.5" width="17" height="13" rx="1.5" fill="#6c6c6c"/>
    <path d="M1 1.5 L9 7.5 L17 1.5" fill="none" stroke="#f8f8f8" stroke-width="1.4"/>
  </svg>
</div>
<nav class="abs footer-nav"><span>POLICY</span><span>FAQ</span><span>TERMS</span><span>SUPPORT</span></nav>
<p class="abs copyright">© 2018 QUILL MARK WORKS All Rights Reserved</p>

</body>
</html>
```